Zielgruppe
Ich biete Marketing und Beratung an. Meine Zielgruppe sind KMU's aber auch Einzelfirmen welche selbst keine Marketingabteilung haben.
Aufgabenstellung
Sie sollen mein bestehendes CI/CD von meiner Website www.velorusk.ch möglichst mit Farben, Formen und Schriften übernehmen. Es soll eine einfache Seite mit 3 Rubriken werden. Über mich / Mein Angebot (Philosophie, Schwerpunkte/Preise) / Kontakt. Impressum, AGB und Datenschutz sollen CH Konform integriert sein. Ich habe meine Domain bei serwanox.ch registriert. Diese soll dann für die neue Website eingerichtet werden und von der Pixolo Seite entfernt werden. Der Link für Kontrabu soll funktionieren. Bilder können von der Pixolo Seite entnommen werden. Da ich für meine Kunden viele Websiten erstellen lassen werde, suche ich einen Designer*in mit welcher ich auch nach dieser Website zusammen arbeiten könnte. Die Seite möchte ich danach selber pflegen können. Es wäre toll wenn sie mit Wordpress erstellt wird (muss aber nicht sein).

```html
<!DOCTYPE html>
<html lang="de">
<head>
<meta charset="utf-8">
<title>Velorusk – Marketing &amp; Beratung</title>
<link rel="stylesheet" href="https://fonts.googleapis.com/css2?family=Barlow+Condensed:wght@600;700;800&family=Inter:wght@400;500;600;700&display=swap">
<style>
:root{
  --green:#12a05c;
  --green-dark:#0e8a4e;
  --mint:#e6f8ee;
  --mint-2:#c9f0da;
  --mint-3:#b6ecd0;
  --ink:#161616;
  --text:#2b2b2b;
  --muted:#6b6b6b;
  --line:#e3e8e5;
  --white:#fff;
}
*{box-sizing:border-box;margin:0;padding:0}
html,body{width:1200px;height:4079px;overflow:hidden}
body{font-family:"Inter",sans-serif;color:var(--text);background:var(--white);position:relative}
.cond{font-family:"Barlow Condensed",sans-serif}
.wrap{position:absolute;left:87px;right:87px}
section,header,footer{position:absolute;left:0;width:1200px}

/* header */
.site-header{top:0;height:66px;background:var(--white);border-bottom:1px solid var(--line)}
.brand{position:absolute;left:101px;top:6px}
.brand-name{font-family:"Inter",sans-serif;font-weight:700;font-size:36px;letter-spacing:-1.5px;color:var(--ink);line-height:44px}
.brand-sub{font-size:7px;color:var(--ink);margin-left:72px;margin-top:-4px;letter-spacing:.3px}
.nav{position:absolute;right:94px;top:17px;display:flex;gap:27px;align-items:center;font-size:12px;font-weight:600;color:var(--ink)}
.nav .btn-nav{background:var(--green);color:#fff;border-radius:18px;padding:9px 20px;font-size:12px}

/* hero */
.hero{top:66px;height:554px;background:linear-gradient(120deg,#f3fcf6 0%,#dcf6e6 55%,#c3efd6 100%);overflow:hidden}
.hero::after{content:"";position:absolute;left:660px;top:-40px;width:700px;height:700px;border-radius:50% 0 0 50%;background:rgba(255,255,255,.28)}
.pill{position:absolute;left:87px;top:64px;background:#fff;border:1px solid var(--line);border-radius:14px;padding:5px 12px 5px 24px;font-size:9px;font-weight:700;color:var(--green);letter-spacing:.3px}
.pill::before{content:"";position:absolute;left:12px;top:9px;width:6px;height:6px;border-radius:50%;background:var(--green)}
.hero h1{position:absolute;left:86px;top:108px;font-family:"Barlow Condensed",sans-serif;font-weight:800;font-size:69px;line-height:58px;color:var(--green);letter-spacing:.5px}
.hero .lead{position:absolute;left:87px;top:322px;width:430px;font-size:16px;line-height:27px;color:var(--ink)}
.btn-row{position:absolute;left:87px;top:416px;display:flex;gap:14px}
.btn{display:flex;align-items:center;gap:8px;height:48px;padding:0 26px;border-radius:7px;font-size:13px;font-weight:600}
.btn-primary{background:var(--green);color:#fff;width:262px;justify-content:center}
.btn-light{background:#fff;color:var(--ink);border:1px solid var(--line)}
.illustration{position:absolute;left:697px;top:105px;width:422px;height:253px;border-radius:10px;background:linear-gradient(135deg,rgba(255,255,255,.55),rgba(18,160,92,.18));z-index:1}
.icon-tile{position:absolute;width:54px;height:54px;border-radius:12px;background:var(--mint-2);display:flex;align-items:center;justify-content:center;z-index:2;box-shadow:0 4px 10px rgba(18,160,92,.15)}
.verified{position:absolute;left:962px;top:105px;width:151px;height:127px;background:#fff;border-radius:10px;box-shadow:0 8px 20px rgba(0,0,0,.08);text-align:center;z-index:2}
.verified .tick{width:40px;height:40px;border-radius:50%;background:var(--green);margin:16px auto 8px;display:flex;align-items:center;justify-content:center}
.verified b{display:block;font-size:14px;color:var(--ink);font-weight:600}
.verified span{font-size:11px;color:var(--ink)}
.chart-card{position:absolute;left:670px;top:371px;width:418px;height:142px;background:#fff;border-radius:10px;box-shadow:0 8px 22px rgba(0,0,0,.08);z-index:2}
.chart-card h4{position:absolute;left:17px;top:17px;font-family:"Barlow Condensed",sans-serif;font-size:16px;font-weight:700;color:var(--ink)}
.chart-card .toggle{position:absolute;right:16px;top:19px;font-size:9px;color:var(--ink);display:flex;align-items:center;gap:6px}
.chart-card .toggle i{width:30px;height:16px;border-radius:8px;background:var(--green);position:relative}
.chart-card .toggle i::after{content:"";position:absolute;right:2px;top:2px;width:12px;height:12px;border-radius:50%;background:#fff}
.months{position:absolute;left:17px;right:17px;bottom:16px;display:flex;justify-content:space-between;font-size:9px;color:var(--ink)}

/* philosophy */
.philo{top:620px;height:713px;background:#fff}
.section-title{font-family:"Barlow Condensed",sans-serif;font-weight:800;color:var(--ink);letter-spacing:.5px}
.philo h2{position:absolute;top:100px;width:100%;text-align:center;font-size:46px}
.philo .kicker{position:absolute;top:162px;width:100%;text-align:center;font-size:14px;font-weight:600;letter-spacing:2px;color:var(--ink)}
.philo-card{position:absolute;top:238px;width:217px;height:180px;border:1px solid var(--line);border-radius:14px;background:#fff;box-shadow:0 4px 10px rgba(0,0,0,.06);text-align:center;overflow:hidden}
.philo-card b{display:block;margin-top:32px;font-family:"Barlow Condensed",sans-serif;font-size:27px;font-weight:800;color:var(--green)}
.philo-card p{font-size:15px;line-height:24px;color:var(--ink);margin-top:4px}
.philo-card svg{position:absolute;right:14px;top:16px;opacity:.12}
.quote{position:absolute;top:508px;width:100%;text-align:center;font-family:"Barlow Condensed",sans-serif;font-weight:600;font-size:28px;line-height:31px;color:var(--ink)}
.quote-mark{position:absolute;left:248px;top:468px;font-family:Georgia,serif;font-size:70px;color:#dfe7e2}
.signature{position:absolute;top:586px;width:100%;display:flex;justify-content:center;align-items:center;gap:14px;font-size:13px;font-weight:600;letter-spacing:1px;color:var(--green)}
.signature::before,.signature::after{content:"";width:40px;height:2px;background:var(--mint-3)}

/* focus + prices background */
.focus{top:1333px;height:1604px;background:linear-gradient(180deg,#e7f8ee 0%,#e4f7ec 60%,#dcf5e6 100%)}
.bar{width:54px;height:5px;background:var(--green)}
.focus .bar{position:absolute;left:87px;top:140px}
.focus h2{position:absolute;left:87px;top:172px;font-size:38px;line-height:34px}
.focus h2 span{color:var(--green)}
.focus .intro{position:absolute;left:87px;top:265px;width:320px;font-size:16px;line-height:27px;color:var(--ink)}
.focus .link{position:absolute;left:87px;top:400px;font-size:13px;font-weight:600;color:var(--green);border-bottom:2px solid var(--green);padding-bottom:3px}
.service{position:absolute;width:308px;height:186px;background:#fff;border:1px solid var(--line);border-radius:8px;padding:26px 27px}
.service .ico{width:46px;height:46px;border-radius:9px;background:var(--mint-2);display:flex;align-items:center;justify-content:center}
.service h3{margin-top:24px;font-family:"Barlow Condensed",sans-serif;font-size:23px;font-weight:700;color:var(--ink)}
.service p{margin-top:8px;font-size:11px;line-height:16px;color:var(--text)}

.prices h2{position:absolute;top:922px;width:100%;text-align:center;font-size:44px}
.prices .bar{position:absolute;left:560px;top:983px;width:80px;height:4px}
.prices .intro{position:absolute;top:1006px;left:270px;width:660px;text-align:center;font-size:15px;line-height:24px;color:var(--ink)}
.price-card{position:absolute;top:1122px;width:412px;height:374px;border-radius:14px;padding:34px 34px}
.price-card.basic{left:174px;background:#fff;box-shadow:0 12px 30px rgba(0,0,0,.08)}
.price-card.featured{left:614px;background:linear-gradient(160deg,#c6f0da,#b2ebcd);border:1px solid #a4e2c2;box-shadow:0 12px 30px rgba(18,160,92,.12)}
.price-card h3{font-family:"Barlow Condensed",sans-serif;font-size:23px;font-weight:700;color:var(--ink)}
.price-card .tag{display:inline-block;margin-top:10px;font-size:10px;font-weight:700;letter-spacing:1px;padding:3px 7px;border-radius:3px;background:#f0f2f1;color:var(--ink)}
.featured .tag{background:rgba(255,255,255,.5);color:#84b99c}
.price-card .amount{position:absolute;right:34px;top:30px;font-size:31px;font-weight:500;color:var(--green)}
.price-card .amount small{font-size:14px;color:var(--ink);margin-left:6px}
.price-card ul{list-style:none;margin-top:52px}
.price-card li{display:flex;align-items:center;gap:14px;font-size:13px;color:var(--ink);height:34px}
.chk{width:15px;height:15px;border-radius:50%;display:flex;align-items:center;justify-content:center;flex:none}
.basic .chk{background:#e9ecea}
.featured .chk{background:var(--green)}
.price-cta{position:absolute;left:34px;right:34px;bottom:34px;height:46px;border-radius:7px;display:flex;align-items:center;justify-content:center;font-size:11px;font-weight:600;letter-spacing:1.2px}
.basic .price-cta{border:2px solid var(--green);color:var(--green)}
.featured .price-cta{background:var(--green);color:#fff;height:44px;bottom:32px}

/* contact */
.contact{top:2937px;height:775px;background:#fff}
.contact h2{position:absolute;left:87px;top:101px;font-size:44px}
.contact .bar{position:absolute;left:87px;top:163px;width:66px;height:4px}
.contact .intro{position:absolute;left:87px;top:186px;width:470px;font-size:16px;line-height:27px;color:var(--ink)}
.info{position:absolute;left:87px;display:flex;gap:20px}
.info .ico{width:46px;height:46px;border-radius:10px;background:var(--mint);display:flex;align-items:center;justify-content:center;flex:none;margin-top:10px}
.info b{display:block;font-family:"Barlow Condensed",sans-serif;font-size:17px;font-weight:700;color:var(--ink)}
.info span{display:block;font-size:13px;line-height:20px;color:var(--ink)}
.info span.big{font-size:15px;line-height:24px}
.divider{position:absolute;left:87px;width:484px;top:562px;height:1px;background:var(--line)}
.portrait{position:absolute;left:87px;top:593px;width:80px;height:80px;border-radius:50%;border:3px solid var(--green);background:linear-gradient(160deg,#eef1ee,#c9cfca)}
.social-note{position:absolute;left:194px;top:601px}
.dot-badge{width:32px;height:32px;border-radius:50%;background:var(--ink);color:#fff;font-size:9px;font-weight:700;display:flex;align-items:center;justify-content:center}
.social-note p{margin-top:4px;font-size:11px;font-style:italic;color:var(--ink)}
.form-card{position:absolute;left:630px;top:110px;width:483px;height:523px;background:#fff;border-radius:14px;box-shadow:0 10px 30px rgba(0,0,0,.07);padding:38px}
.form-card h3{font-family:"Barlow Condensed",sans-serif;font-size:23px;font-weight:700;color:var(--ink)}
.field{height:48px;border:1px solid var(--line);border-radius:6px;background:#f8f9f8;font-size:12px;color:#9a9a9a;padding:15px 13px}
.row{display:flex;gap:19px;margin-top:24px}
.row .field{flex:1}
.field.wide{margin-top:20px}
.field.area{height:126px;margin-top:20px}
.consent{display:flex;gap:10px;margin-top:22px;font-size:10px;line-height:15px;color:var(--ink)}
.consent i{width:11px;height:11px;border:1px solid #999;border-radius:2px;flex:none;margin-top:2px}
.send{margin-top:22px;height:52px;border-radius:7px;background:var(--green);color:#fff;font-size:13px;font-weight:600;display:flex;align-items:center;justify-content:center;gap:8px}

/* footer */
.site-footer{top:3712px;height:367px;background:linear-gradient(110deg,#f4fbf6,#dff6e8 70%,#ccf1dc);border-top:1px solid var(--line)}
.site-footer .brand-name{position:absolute;left:92px;top:62px;font-size:27px;line-height:30px}
.site-footer .about{position:absolute;left:87px;top:125px;width:340px;font-size:13px;line-height:22px;color:var(--ink)}
.foot-col{position:absolute;top:72px}
.foot-col h4{font-family:"Barlow Condensed",sans-serif;font-size:16px;font-weight:700;color:var(--ink)}
.foot-col li{list-style:none;font-size:13px;color:var(--ink);margin-top:14px}
.foot-col li::before{content:"• ";color:var(--green)}
.foot-col .circle{margin-top:22px;width:40px;height:40px;border-radius:50%;background:var(--mint-2);color:var(--green);font-size:10px;font-weight:700;display:flex;align-items:center;justify-content:center}
.foot-bottom{position:absolute;left:87px;right:87px;top:253px;border-top:1px solid #d3e9dc;padding-top:27px;display:flex;justify-content:space-between;font-size:11px;color:var(--ink)}
.heart{color:var(--green)}
</style>
</head>
<body>

<header class="site-header">
  <div class="brand"><div class="brand-name">velorusk</div><div class="brand-sub">MARKETING &amp; BERATUNG</div></div>
  <nav class="nav"><span>ÜBER MICH</span><span>ANGEBOT</span><span>PREISE</span><span class="btn-nav">Kontakt</span></nav>
</header>

<section class="hero">
  <div class="pill">DEIN MARKETING PROFI</div>
  <h1>KLAR.<br>INSPIRIEREND.<br>WIRKSAM.</h1>
  <p class="lead">Durch meine Marketing Expertise hole ich das Beste aus Ihrem Unternehmen heraus.</p>
  <div class="btn-row">
    <div class="btn btn-primary">Kostenlose Offerte verlangen <svg width="12" height="12" viewBox="0 0 24 24" fill="none" stroke="#fff" stroke-width="2.5"><path d="M5 12h14M13 6l6 6-6 6"/></svg></div>
    <div class="btn btn-light"><svg width="13" height="13" viewBox="0 0 24 24" fill="none" stroke="#161616" stroke-width="2"><path d="M12 3 3 8l9 5 9-5-9-5zM3 13l9 5 9-5"/></svg>Mein Angebot</div>
  </div>
  <div class="illustration" role="img" aria-label="Illustration: Beraterin präsentiert vor einem Team an einer Tafel mit Diagrammen"></div>
  <div class="icon-tile" style="left:619px;top:73px"><svg width="22" height="22" viewBox="0 0 24 24" fill="none" stroke="#12a05c" stroke-width="2"><rect x="4" y="3" width="16" height="18" rx="2"/><path d="M9 8h1M14 8h1M9 12h1M14 12h1M10 21v-4h4v4"/></svg></div>
  <div class="icon-tile" style="left:619px;top:190px"><svg width="22" height="22" viewBox="0 0 24 24" fill="none" stroke="#12a05c" stroke-width="2"><path d="M3 11v2h3l6 4V7L6 11H3zM16 9a4 4 0 0 1 0 6"/></svg></div>
  <div class="verified">
    <div class="tick"><svg width="18" height="18" viewBox="0 0 24 24" fill="none" stroke="#fff" stroke-width="3"><path d="M5 12l5 5 9-10"/></svg></div>
    <b>Verified!</b><span>100% Client Satisfied</span>
  </div>
  <div class="chart-card">
    <h4>KMU Wachstum 2026</h4>
    <div class="toggle">Monatlich / Jährlich <i></i></div>
    <svg style="position:absolute;left:46px;top:50px" width="330" height="50" viewBox="0 0 330 50"><path d="M0 44 C30 38 50 40 80 36 S130 38 160 32 200 30 230 24 270 22 290 16 330 12" fill="none" stroke="#12a05c" stroke-width="2"/></svg>
    <div class="months"><span>Jan</span><span>Feb</span><span>Mär</span><span>Apr</span><span>Mai</span><span>Jun</span><span>Jul</span><span>Aug</span><span>Sep</span><span>Okt</span><span>Nov</span><span>Dez</span></div>
  </div>
</section>

<section class="philo">
  <h2 class="section-title">MEINE PHILOSOPHIE</h2>
  <div class="kicker">WAS STEHT HINTER VELORUSK..?</div>
  <div class="philo-card" style="left:247px"><svg width="70" height="70" viewBox="0 0 24 24" fill="none" stroke="#12a05c" stroke-width="2"><path d="M12 19l7-7 3 3-7 7-3-3zM18 13l-1.5-7.5L2 2l3.5 14.5L13 18l5-5z"/></svg><b>VELO</b><p>Branding</p></div>
  <div class="philo-card" style="left:492px"><svg width="70" height="70" viewBox="0 0 24 24" fill="none" stroke="#12a05c" stroke-width="2"><rect x="3" y="7" width="18" height="14" rx="2"/><path d="M8 7V4h8v3"/></svg><b>MARKT</b><p>Business</p></div>
  <div class="philo-card" style="left:736px"><svg width="70" height="70" viewBox="0 0 24 24" fill="none" stroke="#12a05c" stroke-width="2"><path d="M12 3l2 6 6 2-6 2-2 6-2-6-6-2 6-2z"/></svg><b>RUSK</b><p>Erzeugen<br>Erneuern<br>Kreieren</p></div>
  <div class="quote-mark">“</div>
  <p class="quote">Durch meine Marketing Expertise hole ich das Beste aus<br>Ihrem Unternehmen heraus.</p>
  <div class="signature">MIRELKA DONAT</div>
</section>

<section class="focus">
  <div class="bar"></div>
  <h2 class="section-title">MEINE<br><span>SCHWERPUNKTE</span></h2>
  <p class="intro">Als Ihr externer Marketing Partner biete ich maßgeschneiderte Lösungen, die genau dort ansetzen, wo Sie Unterstützung brauchen.</p>
  <div class="link">Jetzt anfragen →</div>

  <div class="service" style="left:475px;top:106px"><div class="ico"><svg width="20" height="20" viewBox="0 0 24 24" fill="none" stroke="#12a05c" stroke-width="2"><circle cx="12" cy="12" r="9"/><circle cx="12" cy="12" r="5"/><circle cx="12" cy="12" r="1.5"/></svg></div><h3>Marketing Strategie</h3><p>Entwicklung zielgerichteter Strategien für nachhaltiges Wachstum.</p></div>
  <div class="service" style="left:804px;top:106px"><div class="ico"><svg width="20" height="20" viewBox="0 0 24 24" fill="none" stroke="#12a05c" stroke-width="2"><path d="M12 3a9 9 0 1 0 0 18c1.5 0 2-1 1.5-2s0-2 1.5-2H18a3 3 0 0 0 3-3c0-6-4-11-9-11z"/><circle cx="8" cy="10" r="1"/><circle cx="12" cy="7" r="1"/><circle cx="16" cy="10" r="1"/></svg></div><h3>Branding</h3><p>Aufbau und Pflege einer starken, unverwechselbaren Marke.</p></div>
  <div class="service" style="left:475px;top:315px"><div class="ico"><svg width="20" height="20" viewBox="0 0 24 24" fill="none" stroke="#12a05c" stroke-width="2"><path d="M12 3l8 4.5v9L12 21l-8-4.5v-9zM12 12l8-4.5M12 12v9M12 12 4 7.5"/></svg></div><h3>Product Management</h3><p>Optimierung Ihres Produktlebenszyklus und Marktpositionierung.</p></div>
  <div class="service" style="left:804px;top:315px"><div class="ico"><svg width="20" height="20" viewBox="0 0 24 24" fill="none" stroke="#12a05c" stroke-width="2"><path d="M3 11v2h3l6 4V7L6 11H3zM16 9a4 4 0 0 1 0 6"/></svg></div><h3>Kommunikation</h3><p>Werbe- und Kommunikationsplanung, die ankommt.</p></div>
  <div class="service" style="left:475px;top:524px"><div class="ico"><svg width="20" height="20" viewBox="0 0 24 24" fill="none" stroke="#12a05c" stroke-width="2"><path d="M3 4h12v8H7l-4 3zM9 15v2h8l4 3V9h-3"/></svg></div><h3>Beratung</h3><p>Persönliche Beratung und Sparringspartner für Ihre Ideen.</p></div>
  <div class="service" style="left:804px;top:524px"><div class="ico"><svg width="20" height="20" viewBox="0 0 24 24" fill="none" stroke="#12a05c" stroke-width="2"><rect x="3" y="4" width="18" height="12" rx="1"/><path d="M12 16v4M8 20h8"/></svg></div><h3>Workshops</h3><p>Events, Workshops und Schulungen für Ihr Team.</p></div>

  <div class="prices">
    <h2 class="section-title">PREISE</h2>
    <div class="bar"></div>
    <p class="intro">Transparenz ist mir wichtig. Jede Zusammenarbeit wird individuell offeriert, basierend auf Ihren Bedürfnissen.</p>
    <div class="price-card basic">
      <h3>Halbtage</h3><span class="tag">PROJEKTBASIS</span>
      <div class="amount">580<small>CHF</small></div>
      <ul>
        <li><span class="chk"><svg width="9" height="9" viewBox="0 0 24 24" fill="none" stroke="#9aa" stroke-width="3"><path d="M5 12l5 5 9-10"/></svg></span>Coaching für spezifische Projekte</li>
        <li><span class="chk"><svg width="9" height="9" viewBox="0 0 24 24" fill="none" stroke="#9aa" stroke-width="3"><path d="M5 12l5 5 9-10"/></svg></span>Mitarbeit direkt im Unternehmen</li>
        <li><span class="chk"><svg width="9" height="9" viewBox="0 0 24 24" fill="none" stroke="#9aa" stroke-width="3"><path d="M5 12l5 5 9-10"/></svg></span>Lancierung von Produkten</li>
        <li><span class="chk"><svg width="9" height="9" viewBox="0 0 24 24" fill="none" stroke="#9aa" stroke-width="3"><path d="M5 12l5 5 9-10"/></svg></span>Relaunch &amp; Marktanalysen</li>
      </ul>
      <div class="price-cta">OFFERTE ANFRAGEN</div>
    </div>
    <div class="price-card featured">
      <h3>Einzelstunden</h3><span class="tag">FLEXIBEL</span>
      <div class="amount">160<small>CHF</small></div>
      <ul>
        <li><span class="chk"><svg width="9" height="9" viewBox="0 0 24 24" fill="none" stroke="#fff" stroke-width="3"><path d="M5 12l5 5 9-10"/></svg></span>Erstellen der Marketing Strategie</li>
        <li><span class="chk"><svg width="9" height="9" viewBox="0 0 24 24" fill="none" stroke="#fff" stroke-width="3"><path d="M5 12l5 5 9-10"/></svg></span>Sortimentsanalysen mit Massnahmen</li>
        <li><span class="chk"><svg width="9" height="9" viewBox="0 0 24 24" fill="none" stroke="#fff" stroke-width="3"><path d="M5 12l5 5 9-10"/></svg></span>Branding &amp; Social Media Inhalte</li>
        <li><span class="chk"><svg width="9" height="9" viewBox="0 0 24 24" fill="none" stroke="#fff" stroke-width="3"><path d="M5 12l5 5 9-10"/></svg></span>Website Beratung</li>
      </ul>
      <div class="price-cta">TERMIN VEREINBAREN</div>
    </div>
  </div>
</section>

<section class="contact">
  <h2 class="section-title">KONTAKT</h2>
  <div class="bar"></div>
  <p class="intro">Bereit für den nächsten Schritt? Ich freue mich darauf, mit Ihnen zusammenzuarbeiten und Ihr Unternehmen voranzubringen.</p>
  <div class="info" style="top:305px"><div class="ico"><svg width="20" height="20" viewBox="0 0 24 24" fill="none" stroke="#12a05c" stroke-width="2"><path d="M12 21s-7-6.5-7-12a7 7 0 0 1 14 0c0 5.5-7 12-7 12z"/><circle cx="12" cy="9" r="2.5"/></svg></div><div><b>Adresse</b><span>Velorusk, Mirelka Donat GmbH</span><span>Lindenhof 4, CH-6300 Talmatt</span></div></div>
  <div class="info" style="top:398px"><div class="ico"><svg width="20" height="20" viewBox="0 0 24 24" fill="none" stroke="#12a05c" stroke-width="2"><path d="M5 4h4l2 5-2.5 1.5a11 11 0 0 0 5 5L15 13l5 2v4a2 2 0 0 1-2 2A16 16 0 0 1 3 6a2 2 0 0 1 2-2z"/></svg></div><div><b>Telefon</b><span class="big">+41 78 555 01 23</span></div></div>
  <div class="info" style="top:475px"><div class="ico"><svg width="20" height="20" viewBox="0 0 24 24" fill="none" stroke="#12a05c" stroke-width="2"><rect x="3" y="5" width="18" height="14" rx="2"/><path d="M3 7l9 6 9-6"/></svg></div><div><b>E-Mail</b><span class="big">info@velorusk.ch</span></div></div>
  <div class="divider"></div>
  <div class="portrait" role="img" aria-label="Porträtfoto der Inhaberin"></div>
  <div class="social-note"><div class="dot-badge">K</div><p>„Auf Kontrabu findest du alles über meinen Background“</p></div>

  <div class="form-card">
    <h3>Schreiben Sie mir</h3>
    <div class="row"><div class="field">Vorname *</div><div class="field">Nachname *</div></div>
    <div class="field wide">E-Mail Adresse *</div>
    <div class="field area">Ihre Nachricht *</div>
    <div class="consent"><i></i><span>Ich stimme zu, dass meine Angaben dauerhaft gespeichert werden.<br>(Datenschutzkonform nach DSG)</span></div>
    <div class="send"><svg width="13" height="13" viewBox="0 0 24 24" fill="none" stroke="#fff" stroke-width="2"><path d="M22 2 11 13M22 2l-7 20-4-9-9-4z"/></svg>Nachricht senden</div>
  </div>
</section>

<footer class="site-footer">
  <div class="brand-name">velorusk</div>
  <p class="about">Velorusk begleitet Schweizer KMUs und Einzelfirmen auf dem Weg zu einer starken Marke und sichtbarem Erfolg. Klar, Inspirierend, Wirksam.</p>
  <div class="foot-col" style="left:620px"><h4>Rechtliches</h4><ul><li>Impressum</li><li>Datenschutzerklärung</li><li>AGB</li></ul></div>
  <div class="foot-col" style="left:886px"><h4>Social Media</h4><div class="circle">K</div></div>
  <div class="foot-bottom"><span>© 2026 Velorusk, Mirelka Donat GmbH. Alle Rechte vorbehalten.</span><span>Made with <span class="heart">♥</span> in Switzerland</span></div>
</footer>

</body>
</html>
```